Pardo Vine Society is a new subscription based wine club in need of a logo and website

We need a logo and website for our new subscription based wine club located in Vancouver, British Columbia. We prepare quarterly wine selections chosen by professionals and deliver them to our members. We also offer customers (members and non-members) the opportunity to purchase 6 bottle cases of our past quarterly selections. We pride ourselves on working with family oriented, organic, sustainable wineries and we would like our website to reflect this.

More specific details can be found in the attached outline (word doc).
Updates

Target Market(s)

Wine drinkers with a preference for organic, biodynamic and sustainable wines. Connoisseurs and wine collectors.

Industry/Entity Type

Alcoholic beverages

Coding

Coded - Design and coding required

Number of Pages Required

5+ page

Colors
F0912C
F2A743
F7CA91
FBE8D2
FDF5EE
EE7325
F08F49
F5BC92
FAE3D3
FDF4ED

Requirements
Must have
• An online shop, ability to readily update the shop

```html
<!DOCTYPE html>
<html lang="en">
<head>
<meta charset="utf-8">
<title>Pardo Vine Society</title>
<link href="https://fonts.googleapis.com/css2?family=Cinzel:wght@400;500&family=Crimson+Text:ital,wght@0,400;1,400&display=swap" rel="stylesheet">
<style>
:root{
  --page:#f4f1ec;
  --sheet:#ffffff;
  --ink:#3b3431;
  --muted:#6f6661;
  --accent:#c9612f;
  --accent-soft:#c7703f;
  --card:#faf7f3;
  --frame:#dcebef;
  --footer:#eaf1f3;
}
*{box-sizing:border-box;margin:0;padding:0}
html,body{width:1200px;height:2223px;overflow:hidden}
body{background:var(--page);font-family:"Crimson Text",Georgia,serif;color:var(--ink);position:relative}
.abs{position:absolute}
.sheet{left:127px;top:0;width:935px;height:2223px;background:var(--sheet)}
.brand{left:151px;top:26px;display:flex;align-items:center;gap:8px;font-family:"Cinzel",serif;font-size:13px;color:var(--accent);letter-spacing:1px}
.brand-dot{width:14px;height:14px;border:1.5px solid var(--accent);border-radius:50%}
.nav{top:34px;font-family:"Cinzel",serif;font-size:9.5px;letter-spacing:1.6px;color:var(--ink)}
.icons{left:922px;top:22px;width:114px;height:62px;border:1px solid var(--ink);display:flex}
.icons span{flex:1;border-right:1px solid var(--ink);display:flex;align-items:center;justify-content:center}
.icons span:last-child{border-right:none}
.photo{display:block}
.hero{left:148px;top:81px;width:892px;height:487px;background:linear-gradient(120deg,#2a1c14,#6b4327 45%,#3a2a20 70%,#8a6a4a)}
.arrow{top:318px}
.tile{top:583px;width:285px;height:220px}
.tile-text{position:absolute;left:23px;top:146px}
.cat{font-style:italic;font-size:10.5px;color:var(--accent-soft)}
.title{font-family:"Cinzel",serif;font-size:11.5px;letter-spacing:1.8px;line-height:15px;color:var(--ink)}
.section-title{left:145px;top:866px;font-family:"Cinzel",serif;font-size:19px;letter-spacing:3.5px}
.btn{left:911px;top:863px;width:130px;height:32px;background:var(--accent);color:#fff;font-family:"Cinzel",serif;font-size:9.5px;letter-spacing:1.8px;display:flex;align-items:center;justify-content:center}
.product{top:922px;width:127px;text-align:center}
.product-shot{height:224px;background:var(--card);position:relative}
.tag{position:absolute;right:18px;top:18px;font-family:"Cinzel",serif;font-size:9px;letter-spacing:1.5px;color:var(--accent-soft)}
.bottle{position:absolute;left:50%;top:40px;transform:translateX(-50%);border-radius:8px 8px 4px 4px}
.product .cat{margin-top:17px;font-size:10px}
.product .title{margin-top:4px;font-size:11px;letter-spacing:1.6px}
.price{font-style:italic;font-size:11px;margin-top:5px}
.price s{color:var(--muted);margin-left:3px}
.types{left:145px;top:1264px;width:896px;height:177px;border:5px solid var(--frame)}
.type{top:1292px;width:100px;text-align:center}
.type-art{width:30px;height:96px;margin:0 auto;background:linear-gradient(#e4e4e4,#bdbdbd);border-radius:10px 10px 4px 4px;opacity:.8}
.type .cat{margin-top:16px;font-size:10.5px}
.tour{left:145px;top:1464px;width:896px;height:364px;background:linear-gradient(110deg,#2b211c,#5b4336 40%,#8a6a58 60%,#2a1f1a)}
.play{left:551px;top:1604px;width:82px;height:82px;border:1.5px solid rgba(255,255,255,.8);border-radius:50%}
.tour-title{left:177px;top:1757px;font-family:"Cinzel",serif;font-size:19px;letter-spacing:3.5px;color:#fff}
.tour-sub{left:177px;top:1784px;font-style:italic;font-size:10px;color:#f0a173}
.footer{left:144px;top:1849px;width:896px;height:343px;background:var(--footer)}
.footer-brand{left:160px;top:2010px;display:flex;align-items:center;gap:8px;font-family:"Cinzel",serif;font-size:13px;color:var(--accent)}
.col-title{top:1937px;font-family:"Cinzel",serif;font-size:15px;letter-spacing:2.8px}
.col-item{font-size:11.5px;color:var(--muted);display:flex;align-items:center;gap:7px}
.news-title{font-family:"Cinzel",serif;font-size:10.5px;letter-spacing:1.8px}
.sketch{left:414px;top:2063px;width:354px;height:73px;background:linear-gradient(#eaf1f3,#d5dde0);opacity:.7}
.copyright{left:144px;top:2161px;width:896px;text-align:center;font-size:9.5px;color:var(--muted)}
.copyright em{color:var(--accent-soft)}
.to-top{left:1116px;top:2143px;width:31px;height:31px;background:#d9632e;display:flex;align-items:center;justify-content:center}
</style>
</head>
<body>
<div class="abs sheet"></div>

<header>
  <div class="abs brand"><span class="brand-dot"></span>Pardo Vine Society</div>
  <nav>
    <span class="abs nav" style="left:567px">– Home –</span>
    <span class="abs nav" style="left:641px">About Us</span>
    <span class="abs nav" style="left:727px">Shop</span>
    <span class="abs nav" style="left:787px">Events</span>
    <span class="abs nav" style="left:860px">Blog</span>
  </nav>
  <div class="abs icons">
    <span><svg width="14" height="13" viewBox="0 0 14 13"><path d="M7 12 1.5 6.5A3 3 0 0 1 7 2.5a3 3 0 0 1 5.5 4Z" fill="none" stroke="#3b3431"/></svg></span>
    <span><svg width="16" height="14" viewBox="0 0 16 14"><path d="M1 2h2l2 7h8l1.5-5H4" fill="none" stroke="#3b3431"/><circle cx="4" cy="11" r="2.5" fill="#c9612f"/></svg></span>
    <span><svg width="12" height="12" viewBox="0 0 12 12"><path d="M2 1v10M6 1v10M10 1v10" stroke="#3b3431"/></svg></span>
  </div>
</header>

<section>
  <div class="abs photo hero" role="img" aria-label="Whisky bottles and tasting glasses on a bar beside a chalkboard sign"></div>
  <svg class="abs arrow" style="left:167px" width="32" height="12"><path d="M31 6H1M6 1 1 6l5 5" fill="none" stroke="#fff"/></svg>
  <svg class="abs arrow" style="left:989px" width="32" height="12"><path d="M1 6h30M26 1l5 5-5 5" fill="none" stroke="#fff"/></svg>
</section>

<section>
  <div class="abs tile" style="left:145px;background:linear-gradient(135deg,#f1efec,#e6e2dd)" role="img" aria-label="Prosecco bottle and cork on a pale stone surface">
    <div class="tile-text"><div class="cat">Red wine ~ Dry</div><div class="title">Lorem Brandy<br>Year Old</div></div>
  </div>
  <div class="abs tile" style="left:450px;background:linear-gradient(135deg,#f4f4f2 40%,#d9cca8 75%,#b7a37a)" role="img" aria-label="White wine swirling in a glass">
    <div class="tile-text"><div class="cat">Red wine ~ Desert</div><div class="title">Lorem Brandy<br>Year Old</div></div>
  </div>
  <div class="abs tile" style="left:756px;background:linear-gradient(135deg,#f4f3f1 40%,#8a5a38 75%,#3a2217)" role="img" aria-label="Aged brandy bottle neck with a thirteen year label">
    <div class="tile-text"><div class="cat">Dry ~ Desert</div><div class="title">Lorem Brandy<br>Year Old</div></div>
  </div>
</section>

<section>
  <h2 class="abs section-title">Featured Spirits</h2>
  <div class="abs btn">See More</div>

  <div class="abs product" style="left:145px">
    <div class="product-shot"><span class="tag">Sale</span><div class="bottle" style="width:30px;height:152px;background:linear-gradient(90deg,#2a0f14,#4a1a22)" role="img" aria-label="Red wine bottle"></div></div>
    <div class="cat">Brandy ~ Drink ~ Italy ~ New</div><div class="title">Luctuson<br>Chardonnayy</div><div class="price">65$ <s>85$</s></div>
  </div>
  <div class="abs product" style="left:299px">
    <div class="product-shot"><div class="bottle" style="width:30px;height:152px;background:linear-gradient(90deg,#e07b52,#f2a77f)" role="img" aria-label="Rosé wine bottle"></div></div>
    <div class="cat">Brandy ~ Drink ~ Italy ~ New</div><div class="title">New Cabernet<br>Sauvignon</div><div class="price">67$</div>
  </div>
  <div class="abs product" style="left:452px">
    <div class="product-shot"><span class="tag">New</span><div class="bottle" style="top:52px;width:64px;height:118px;border-radius:20px 20px 22px 22px;background:linear-gradient(90deg,#b45a2a,#e08a52)" role="img" aria-label="Cognac decanter"></div></div>
    <div class="cat">Drink ~ Italy ~ New</div><div class="title">Belasco Llama<br>Cognac</div><div class="price">74$</div>
  </div>
  <div class="abs product" style="left:607px">
    <div class="product-shot"><div class="bottle" style="width:30px;height:152px;background:linear-gradient(90deg,#6a7a1e,#a4b04a)" role="img" aria-label="White wine bottle"></div></div>
    <div class="cat">Brandy ~ Drink ~ Italy ~ New</div><div class="title">La Sauvignon<br>Blanc Wine</div><div class="price">85$</div>
  </div>
  <div class="abs product" style="left:760px">
    <div class="product-shot"><span class="tag">Sale</span><div class="bottle" style="width:46px;height:152px;background:linear-gradient(90deg,#6a0f14,#b0362a)" role="img" aria-label="Bourbon bottle"></div></div>
    <div class="cat">Brandy ~ Drink ~ Italy ~ New</div><div class="title">Heavyweight<br>Cabernet Sauv.</div><div class="price">53$ <s>63$</s></div>
  </div>
  <div class="abs product" style="left:914px">
    <div class="product-shot"><span class="tag">Sold</span><div class="bottle" style="top:60px;width:28px;height:112px;background:linear-gradient(90deg,#d06a42,#efa27a)" role="img" aria-label="Small rosé bottle"></div></div>
    <div class="cat">Brandy ~ Drink ~ Italy ~ New</div><div class="title">Alias Secret Red<br>Blend</div><div class="price">63$</div>
  </div>
</section>

<section>
  <div class="abs types"></div>
  <div class="abs type" style="left:176px"><div class="type-art" role="img" aria-label="Sketch of a red wine bottle"></div><div class="cat">Red Wine</div></div>
  <div class="abs type" style="left:323px"><div class="type-art" role="img" aria-label="Sketch of a white wine bottle"></div><div class="cat">White Wine</div></div>
  <div class="abs type" style="left:470px"><div class="type-art" style="width:36px" role="img" aria-label="Sketch of a whiskey bottle"></div><div class="cat">Whiskey</div></div>
  <div class="abs type" style="left:616px"><div class="type-art" style="width:34px" role="img" aria-label="Sketch of a scotch bottle"></div><div class="cat">Scotch</div></div>
  <div class="abs type" style="left:763px"><div class="type-art" style="width:42px" role="img" aria-label="Sketch of a tequila bottle"></div><div class="cat">Tequila</div></div>
  <div class="abs type" style="left:910px"><div class="type-art" role="img" aria-label="Sketch of a champagne bottle"></div><div class="cat">Champagne</div></div>
</section>

<section>
  <div class="abs tour" role="img" aria-label="Two guests toasting with rosé wine over a cheese board"></div>
  <div class="abs play"><svg width="82" height="82"><path d="M37 35l9 6-9 6Z" fill="#fff"/></svg></div>
  <h2 class="abs tour-title">Take a Tour</h2>
  <div class="abs tour-sub">Porta nibh venenatis cras sed</div>
</section>

<footer>
  <div class="abs footer"></div>
  <div class="abs footer-brand"><span class="brand-dot"></span>Pardo Vine Society</div>

  <h3 class="abs col-title" style="left:371px">Contact Us</h3>
  <div class="abs col-item" style="left:371px;top:1968px"><svg width="13" height="13"><path d="M6.5 12S2 7.5 2 5a4.5 4.5 0 0 1 9 0c0 2.5-4.5 7-4.5 7Z" fill="none" stroke="#c7703f"/><circle cx="6.5" cy="5" r="1.5" fill="none" stroke="#c7703f"/></svg>218 Larch Avenue Vancouver</div>
  <div class="abs col-item" style="left:371px;top:1991px"><svg width="13" height="13"><rect x="1" y="3" width="11" height="8" fill="none" stroke="#c7703f"/><path d="M1 3l5.5 4.5L12 3" fill="none" stroke="#c7703f"/></svg>info@pardovinesociety.com</div>
  <div class="abs col-item" style="left:371px;top:2014px"><svg width="13" height="13"><rect x="3.5" y="1" width="6" height="11" rx="1" fill="none" stroke="#c7703f"/></svg>+(604) 555-0142</div>

  <h3 class="abs col-title" style="left:599px">About Us</h3>
  <div class="abs col-item" style="left:599px;top:1967px">Story about us</div>
  <div class="abs col-item" style="left:599px;top:1991px">Our latest blog posts</div>
  <div class="abs col-item" style="left:599px;top:2014px">Purchase our products</div>
  <div class="abs col-item" style="left:599px;top:2037px">Keep in touch</div>

  <h3 class="abs col-title" style="left:826px">Latest News</h3>
  <div class="abs cat" style="left:826px;top:1968px">September 11, 2021</div>
  <div class="abs news-title" style="left:826px;top:1985px">Largest Vineyard</div>
  <div class="abs cat" style="left:826px;top:2012px">September 11, 2021</div>
  <div class="abs news-title" style="left:826px;top:2029px">Our Best Aperitifs</div>
  <div class="abs cat" style="left:826px;top:2056px">September 11, 2021</div>
  <div class="abs news-title" style="left:826px;top:2073px">Amazing Recipes</div>

  <div class="abs sketch" role="img" aria-label="Faint sketch of a vineyard estate and hills"></div>
  <div class="abs copyright">© 2021 <em>Pardo Vine Society</em>, All Rights Reserved</div>
  <div class="abs to-top"><svg width="14" height="8"><path d="M1 7l6-6 6 6" fill="none" stroke="#fff" stroke-width="1.3"/></svg></div>
</footer>
</body>
</html>
```